Redesign of dating app main page

Task is redesign of main page of dating app. Page design is attached. UX design should be the same (buttons of the top of screen , scrolling down). Searching users profiles with their buttons should be more divided.

```html
<!DOCTYPE html>
<html lang="en">
<head>
<meta charset="utf-8">
<title>Dating App – Discover</title>
<link href="https://fonts.googleapis.com/css2?family=Inter:wght@400;500;600&display=swap" rel="stylesheet">
<style>
  :root {
    --page-bg: #444444;
    --screen-bg: #ffffff;
    --header-bg: #f2f2f2;
    --card-bg: #efefef;
    --accent: #e27512;
    --accent-warm: #f7781e;
    --accent-light: #fbd35a;
    --text-main: #1b1b1b;
    --text-muted: #7a7a7a;
    --close-icon: #3a4a8c;
  }
  * { box-sizing: border-box; margin: 0; padding: 0; }
  html, body {
    width: 859px; height: 1200px; overflow: hidden;
    background: var(--page-bg);
    font-family: "Inter", Arial, sans-serif;
  }
  .screen {
    position: absolute; left: 228px; top: 164px;
    width: 402px; height: 872px;
    background: var(--screen-bg);
    border-radius: 52px; overflow: hidden;
  }
  .header-shape { position: absolute; left: 0; top: 0; }
  .status-bar {
    position: absolute; left: 37px; right: 28px; top: 42px;
    display: flex; justify-content: space-between; align-items: center;
    font-size: 14px; font-weight: 600; color: var(--text-main);
  }
  .nav { position: absolute; top: 0; left: 0; width: 100%; }
  .nav-btn {
    position: absolute; width: 45px; height: 45px; border-radius: 50%;
    background: var(--accent); display: flex; align-items: center; justify-content: center;
  }
  .nav-btn.profile { left: 107px; top: 93px; }
  .nav-btn.messages { left: 264px; top: 93px; }
  .nav-btn.likes {
    left: 174px; top: 79px; width: 66px; height: 66px; background: #fff;
    box-shadow: 0 2px 10px rgba(0,0,0,0.04);
  }
  .profile-card {
    position: absolute; left: 35px; width: 338px;
    border-radius: 20px; overflow: hidden; background: var(--card-bg);
  }
  .profile-card.first { top: 169px; }
  .profile-card.second { top: 609px; left: 33px; height: 300px; }
  .photo { position: relative; width: 100%; height: 331px; }
  .first .photo { background: linear-gradient(160deg, #c98d5f 0%, #7d8a56 35%, #3f5a34 70%, #2c3c27 100%); }
  .second .photo { height: 100%; background: linear-gradient(180deg, #8e9aa6 0%, #c9a173 40%, #6b4a34 70%, #66b5de 100%); }
  .close-btn {
    position: absolute; top: 14px; right: 16px; width: 29px; height: 29px;
    border-radius: 50%; background: rgba(255,255,255,0.9);
    display: flex; align-items: center; justify-content: center;
  }
  .distance {
    position: absolute; right: 20px; bottom: 17px;
    display: flex; flex-direction: column; align-items: center; gap: 4px;
    color: #fff; font-size: 11px; font-weight: 500;
  }
  .info {
    height: 85px; display: flex; align-items: center; justify-content: space-between;
    padding: 0 19px 0 26px;
  }
  .name { font-size: 19px; font-weight: 500; color: var(--text-main); }
  .age { color: var(--text-muted); font-weight: 400; }
  .role { font-size: 12px; color: var(--text-main); margin-top: 3px; }
  .request-btn {
    width: 122px; height: 42px; border-radius: 12px; border: none;
    background: linear-gradient(90deg, var(--accent-warm), var(--accent-light));
    color: #fff; font-family: inherit; font-size: 12px; font-weight: 500;
  }
</style>
</head>
<body>
  <main class="screen">
    <svg class="header-shape" width="402" height="260" viewBox="0 0 402 260">
      <path d="M0 0 H402 V220 Q201 195 0 230 Z" fill="var(--header-bg)"/>
    </svg>

    <div class="status-bar">
      <span class="time">9:41</span>
      <svg width="68" height="12" viewBox="0 0 68 12">
        <rect x="0" y="8" width="3" height="4" rx="1" fill="#1b1b1b"/>
        <rect x="5" y="6" width="3" height="6" rx="1" fill="#1b1b1b"/>
        <rect x="10" y="3" width="3" height="9" rx="1" fill="#1b1b1b"/>
        <rect x="15" y="0" width="3" height="12" rx="1" fill="#1b1b1b"/>
        <path d="M23 4 Q30 -2 37 4 M25.5 6.5 Q30 3 34.5 6.5" stroke="#1b1b1b" stroke-width="1.8" fill="none"/>
        <circle cx="30" cy="10" r="1.6" fill="#1b1b1b"/>
        <rect x="43" y="1" width="21" height="10" rx="3" fill="none" stroke="#1b1b1b"/>
        <rect x="45" y="3" width="17" height="6" rx="1.5" fill="#1b1b1b"/>
        <rect x="65" y="4" width="2" height="4" rx="1" fill="#1b1b1b"/>
      </svg>
    </div>

    <nav class="nav">
      <span class="nav-btn profile">
        <svg width="22" height="22" viewBox="0 0 24 24" fill="none" stroke="#fff" stroke-width="1.6">
          <circle cx="12" cy="8" r="4"/><path d="M4 21 Q4 14 12 14 Q20 14 20 21 Z"/>
        </svg>
      </span>
      <span class="nav-btn likes">
        <svg width="36" height="32" viewBox="0 0 24 22" fill="none" stroke="#1b1b1b" stroke-width="1.4">
          <path d="M12 20 L3.5 11.5 A5 5 0 0 1 12 4.5 A5 5 0 0 1 20.5 11.5 Z"/>
        </svg>
      </span>
      <span class="nav-btn messages">
        <svg width="24" height="22" viewBox="0 0 24 22" fill="none" stroke="#fff" stroke-width="1.5">
          <path d="M3 3 H21 V16 H9 L5 19.5 V16 H3 Z"/>
          <path d="M7 7.5 H17 M7 11 H14"/>
        </svg>
      </span>
    </nav>

    <article class="profile-card first">
      <div class="photo" role="img" aria-label="Portrait photo of a smiling woman with shoulder-length blonde hair outdoors">
        <span class="close-btn">
          <svg width="10" height="10" viewBox="0 0 10 10" stroke="var(--close-icon)" stroke-width="1.3"><path d="M1 1 L9 9 M9 1 L1 9"/></svg>
        </span>
        <span class="distance">
          <svg width="16" height="21" viewBox="0 0 16 21"><path d="M8 0 A8 8 0 0 1 16 8 C16 13 8 21 8 21 C8 21 0 13 0 8 A8 8 0 0 1 8 0 Z" fill="#f28a1f"/><circle cx="8" cy="8" r="3" fill="#fff"/></svg>
          10km
        </span>
      </div>
      <div class="info">
        <div>
          <h2 class="name">Lucia Moreno <span class="age">25</span></h2>
          <p class="role">Developer</p>
        </div>
        <button class="request-btn">Send Request</button>
      </div>
    </article>

    <article class="profile-card second">
      <div class="photo" role="img" aria-label="Portrait photo of a young man in a light blue shirt resting his chin on his hand">
        <span class="close-btn">
          <svg width="10" height="10" viewBox="0 0 10 10" stroke="var(--close-icon)" stroke-width="1.3"><path d="M1 1 L9 9 M9 1 L1 9"/></svg>
        </span>
      </div>
    </article>
  </main>
</body>
</html>
```